A Clear Three Step Roadmap For Contractors

We are looking for a one-pager "roadmap" that is similar to the 2nd picture we attached, but much more professional & better... please make it landscape orientation. The logo for this system is attached below, as well.

Our Brand Colors to use:
#f2d582
#303030
#8b8c90

The copy we'd like to use on the flyer:
A Clear Three Step Roadmap that will finally allow you to attract quality customers and win more jobs.

The Keystone Ladder Method is a simple to follow system that was created specifically for Contractors and Blue Collar Business Owners.

When it comes to marketing and growing their business, the majority of Contractors are left confused, frustrated and extremely overwhelmed. Unlike most sales, marketing & training programs that offer a single "piece of the puzzle", we've mapped out each essential step of the puzzle and cut out all of the fluff.

All you have to do is complete each step in the right order and we'll be guiding you along the entire journey!

A ---> B

Blueprint: Get clear on where you're going, define your ideal audience, and finally, master your message.
Step 1: Clarify The Chaos
Step 2: Define Your Customer
Step 3: Master Your Message

Build: Attract quality leads, Build your funnel and Formulate a high-converting follow-up system
Step 4: Develop Lead Generator
Step 5: Construct Your Funnel
Step 6: Formulate the Follow-Up

Breakthrough: Get in front of your ideal customers and rapidly scale your business by driving traffic and becoming the authority in your market
Step 7: Turn-On the Traffic
Step 8: Become the Authority
Step 9: Unlock Your Growth

```html
<!DOCTYPE html>
<html lang="en">
<head>
<meta charset="utf-8">
<title>Keystone Ladder Method – Roadmap</title>
<link href="https://fonts.googleapis.com/css2?family=Montserrat:wght@600;700;800&display=swap" rel="stylesheet">
<style>
  :root {
    --gold: #f2d582;
    --charcoal: #303030;
    --steel: #8b8c90;
    --card-dark: #161616;
    --card-mid: #262626;
    --line: #ffffff;
    --backdrop: #9d9d9d;
    --inner-light: #f1f1f1;
    --inner-shade: #b9b9bb;
  }
  html, body {
    margin: 0;
    width: 1200px;
    height: 1000px;
    overflow: hidden;
    background: var(--backdrop);
  }
  .roadmap-card {
    position: absolute;
    left: 0;
    top: 126px;
    width: 1200px;
    height: 748px;
    display: block;
  }
  .brand-name {
    font-family: "Montserrat", sans-serif;
    font-weight: 800;
    font-size: 30px;
    fill: var(--gold);
    letter-spacing: 0.5px;
  }
  .phase-title {
    font-family: "Montserrat", sans-serif;
    font-weight: 800;
    font-size: 21px;
    fill: var(--gold);
  }
  .step-label {
    font-family: "Montserrat", sans-serif;
    font-weight: 700;
    font-size: 14.5px;
    fill: var(--gold);
    text-anchor: middle;
  }
  .footer-name {
    font-family: "Montserrat", sans-serif;
    font-weight: 600;
    font-size: 11.5px;
    fill: #ffffff;
  }
  .route { fill: none; stroke: var(--line); stroke-width: 3; }
  .node-ring { fill: #0d0d0d; stroke: var(--line); stroke-width: 3; }
  .node-gold { fill: var(--gold); }
  .node-core { fill: url(#coreShade); stroke: #ffffff; stroke-width: 2; }
  .icon { fill: var(--charcoal); stroke: none; }
  .icon-line { fill: none; stroke: var(--charcoal); stroke-width: 3; stroke-linecap: round; }
</style>
</head>
<body>
<svg class="roadmap-card" viewBox="0 0 1015 633" xmlns="http://www.w3.org/2000/svg" aria-label="Keystone Ladder Method three step roadmap">
  <defs>
    <radialGradient id="cardTone" cx="50%" cy="40%" r="75%">
      <stop offset="0" stop-color="var(--card-mid)"/>
      <stop offset="1" stop-color="var(--card-dark)"/>
    </radialGradient>
    <radialGradient id="coreShade" cx="40%" cy="35%" r="70%">
      <stop offset="0" stop-color="var(--inner-light)"/>
      <stop offset="1" stop-color="var(--inner-shade)"/>
    </radialGradient>
    <g id="node">
      <circle class="node-ring" r="50"/>
      <circle class="node-gold" r="44"/>
      <circle class="node-core" r="32"/>
    </g>
  </defs>

  <rect class="card-surface" width="1015" height="633" fill="url(#cardTone)"/>

  <!-- Brand heading -->
  <g class="brand-heading">
    <rect x="292" y="47" width="28" height="28" fill="var(--gold)"/>
    <text class="brand-name" x="332" y="72">KEYSTONE LADDER METHOD</text>
  </g>

  <!-- Route -->
  <path class="route" d="M813 170 H167 Q147 170 147 190 V317 Q147 337 167 337 H850 Q870 337 870 357 V484 Q870 504 850 504 H200"/>

  <!-- Phase titles -->
  <text class="phase-title" x="144" y="153">BREAKTHROUGH</text>
  <text class="phase-title" x="144" y="367">BUILD</text>
  <text class="phase-title" x="735" y="538">BLUEPRINT</text>

  <!-- Breakthrough steps -->
  <g transform="translate(426 170)">
    <use href="#node"/>
    <rect class="icon" x="-13" y="-16" width="22" height="30" rx="2"/>
    <path d="M-8 -9 H4 M-8 -3 H4 M-8 3 H4 M-8 9 H0" stroke="#e8e8e8" stroke-width="2"/>
    <path class="icon" d="M11 -12 h5 v22 l-2.5 5 l-2.5 -5z"/>
  </g>
  <text class="step-label" x="426" y="242">Turn-On the</text>
  <text class="step-label" x="426" y="260">Traffic</text>

  <g transform="translate(621 170)">
    <use href="#node"/>
    <path class="icon" d="M-14 12 V-2 A14 14 0 0 1 14 -2 V12 Z"/>
    <rect class="icon" x="-17" y="12" width="34" height="5" rx="2"/>
    <circle r="6" fill="none" stroke="#e8e8e8" stroke-width="2.5" cy="0"/>
  </g>
  <text class="step-label" x="621" y="242">Become</text>
  <text class="step-label" x="621" y="260">the Authority</text>

  <g transform="translate(813 170)">
    <use href="#node"/>
    <rect class="icon" x="-14" y="4" width="7" height="12"/>
    <rect class="icon" x="-4" y="-2" width="7" height="18"/>
    <rect class="icon" x="6" y="-8" width="7" height="24"/>
    <path class="icon" d="M-16 0 L-2 -14 L-6 -18 L4 -20 L2 -10 L-2 -13 L-14 2 Z"/>
  </g>
  <text class="step-label" x="813" y="242">Unlock Your</text>
  <text class="step-label" x="813" y="260">Growth</text>

  <!-- Build steps -->
  <g transform="translate(317 337)">
    <use href="#node"/>
    <rect class="icon" x="-17" y="-15" width="30" height="26" rx="2"/>
    <path d="M-13 -8 H9 M-13 -2 H9 M-13 4 H3" stroke="#e8e8e8" stroke-width="2"/>
    <circle class="icon" cx="12" cy="11" r="8"/>
    <text x="12" y="15" font-family="Montserrat, sans-serif" font-size="10" font-weight="700" fill="#e8e8e8" text-anchor="middle">fx</text>
  </g>
  <text class="step-label" x="317" y="409">Formulate the</text>
  <text class="step-label" x="317" y="427">Follow-Up</text>

  <g transform="translate(509 337)">
    <use href="#node"/>
    <path class="icon" d="M-10 -8 A10 10 0 0 1 10 -8 Z"/>
    <path class="icon" d="M-18 -5 H18 L4 8 V17 L-4 13 V8 Z"/>
  </g>
  <text class="step-label" x="509" y="409">Construct</text>
  <text class="step-label" x="509" y="427">Your Funnel</text>

  <g transform="translate(703 337)">
    <use href="#node"/>
    <path class="icon-line" d="M-6 -12 L-14 -4 A11 11 0 0 0 2 12 L10 4" stroke-width="8" stroke-linecap="butt"/>
    <path d="M6 -14 l6 -4 M12 -8 l6 -2 M10 -2 l6 0" stroke="var(--charcoal)" stroke-width="2"/>
  </g>
  <text class="step-label" x="703" y="409">Develop Lead</text>
  <text class="step-label" x="703" y="427">Generator</text>

  <!-- Blueprint steps -->
  <g transform="translate(200 504)">
    <use href="#node"/>
    <circle class="icon-line" r="14"/>
    <circle class="icon" r="8"/>
    <path class="icon-line" d="M0 -20 V-14 M0 14 V20 M-20 0 H-14 M14 0 H20"/>
  </g>
  <text class="step-label" x="200" y="578">Clarify The</text>
  <text class="step-label" x="200" y="596">Chaos</text>

  <g transform="translate(395 504)">
    <use href="#node"/>
    <circle class="icon" cx="0" cy="-8" r="5"/>
    <circle class="icon" cx="-11" cy="-5" r="4"/>
    <circle class="icon" cx="11" cy="-5" r="4"/>
    <path class="icon" d="M-17 12 A17 17 0 0 1 17 12 Z"/>
    <circle r="5" cy="8" fill="#e8e8e8"/>
  </g>
  <text class="step-label" x="395" y="578">Define Your</text>
  <text class="step-label" x="395" y="596">Customer</text>

  <g transform="translate(588 504)">
    <use href="#node"/>
    <ellipse class="icon" cx="-5" cy="-4" rx="12" ry="10"/>
    <path class="icon" d="M-12 3 L-15 12 L-5 5 Z"/>
    <ellipse class="icon" cx="7" cy="5" rx="11" ry="9" stroke="#e8e8e8" stroke-width="2"/>
    <path class="icon" d="M12 11 L16 18 L7 13 Z"/>
  </g>
  <text class="step-label" x="588" y="578">Master Your</text>
  <text class="step-label" x="588" y="596">Message</text>

  <!-- Footer mark -->
  <g class="footer-brand">
    <rect x="688" y="590" width="9" height="9" fill="var(--gold)"/>
    <text class="footer-name" x="701" y="599">Keystone Ladder Method</text>
  </g>
</svg>
</body>
</html>
```